Kindled Harvest Christian Ministry needs a Conference Ad

We are a Christian nonprofit focused on eliminating systemic poverty and helping believers function as ministers in their workplaces. The 2025 Kindled Harvest Global Conference coming up in October, and we need an ad for social media (facebook, instagram, and X) and our website in order to get people excited to attend! We are looking for a modern and sleek design that incorporates our logo (attached file). You can either put just the butterfly and then write our company name separately somewhere in the design or use it as is (we used Gotham font for the logo). We want to emphasize the joy of in-person connection at the conference, so you could possibly include stock photos of young people gathering together. You could also include the attached photo of our founders in the design and say “with Len and Marta Drubeck". Also, include the conference dates, which are October 9-12, 2025, and say “come in person or join online”. Lastly, please include the tagline “from the Coastal Awakening to Worldwide Transformation”. NOTE: I’m attaching AN EXAMPLE I’ve created of how the design could look, which you can feel free to use for inspiration.
Target Market(s)
Young people on Instagram and facebook
Font styles to use
Other font styles liked:
- Gotham
Look and feel

```html
<!DOCTYPE html>
<html lang="en">
<head>
<meta charset="utf-8">
<title>Kindled Harvest Global Conference</title>
<link rel="stylesheet" href="https://fonts.googleapis.com/css2?family=Anton&family=Montserrat:wght@800;900&display=swap">
<style>
  :root {
    --surround: #2a2a2a;
    --gold: #ffc000;
    --ink: #000000;
    --paper: #ffffff;
    --photo-cool-a: #eef0f3;
    --photo-cool-b: #3a3f4c;
    --photo-warm-a: #efe7dc;
    --photo-warm-b: #2a2624;
  }
  html, body {
    margin: 0;
    padding: 0;
    width: 1200px;
    height: 1036px;
    overflow: hidden;
    background: var(--surround);
  }
  .ad {
    position: absolute;
    left: 75px;
    top: 78px;
    width: 1050px;
    height: 880px;
    background: var(--gold);
    color: var(--ink);
    overflow: hidden;
  }
  .ministry-name {
    position: absolute;
    left: 0;
    right: 0;
    top: 56px;
    margin: 0;
    text-align: center;
    font-family: "Montserrat", sans-serif;
    font-weight: 900;
    font-size: 62px;
    line-height: 1;
    letter-spacing: 1px;
  }
  .hosts {
    position: absolute;
    left: 0;
    right: 0;
    top: 177px;
    margin: 0;
    text-align: center;
    font-family: "Montserrat", sans-serif;
    font-weight: 800;
    font-size: 38px;
    line-height: 42px;
  }
  .photo {
    position: absolute;
    top: 275px;
    width: 262px;
    height: 488px;
    border-radius: 26px;
  }
  .photo--gathering {
    left: 245px;
    background: linear-gradient(160deg, var(--photo-cool-a) 0%, #c9ccd3 45%, var(--photo-cool-b) 100%);
  }
  .photo--founders {
    left: 543px;
    background: linear-gradient(200deg, var(--photo-warm-a) 0%, #c7a98a 45%, var(--photo-warm-b) 100%);
  }
  .dates {
    position: absolute;
    left: 58px;
    top: 522px;
    width: 180px;
    font-family: "Anton", sans-serif;
    text-align: center;
    line-height: 1;
  }
  .dates__days { display: block; font-size: 96px; line-height: 92px; }
  .dates__month { display: block; font-size: 45px; line-height: 44px; }
  .dates__year { display: block; font-size: 48px; line-height: 48px; letter-spacing: 14px; margin-right: -14px; }
  .attend {
    position: absolute;
    right: 58px;
    top: 530px;
    margin: 0;
    font-family: "Anton", sans-serif;
    font-size: 58px;
    line-height: 60px;
    text-align: left;
  }
  .tagline-band {
    position: absolute;
    left: 0;
    right: 0;
    top: 745px;
    height: 70px;
    background: var(--ink);
    display: flex;
    align-items: center;
    justify-content: center;
  }
  .tagline {
    margin: 0;
    color: var(--paper);
    font-family: "Anton", sans-serif;
    font-size: 38px;
    line-height: 1;
    letter-spacing: 0.3px;
  }
</style>
</head>
<body>
  <main class="ad">
    <h1 class="ministry-name">KINDLED HARVEST</h1>
    <p class="hosts">WITH LEN AND MARTA<br>DRUBECK</p>

    <div class="photo photo--gathering" role="img" aria-label="Stock photo of young professionals gathering and sharing a tablet in a bright hall"></div>
    <div class="photo photo--founders" role="img" aria-label="Photo of the founders Len and Marta Drubeck smiling together"></div>

    <p class="dates">
      <span class="dates__days">9-12</span>
      <span class="dates__month">OCTOBER</span>
      <span class="dates__year">2025</span>
    </p>

    <p class="attend">COME IN<br>PERSON<br>OR JOIN</p>

    <div class="tagline-band">
      <p class="tagline">From the Coastal Awakening to Worldwide Transformation</p>
    </div>
  </main>
</body>
</html>
```